Real Estate Web Page Redesign

We are a small town real estate agency in need of a web site redesign. To give you a little background on our agency…our target is middle income households and farmers. Our staff includes real estate agents and an auctioneer. We’ve been in business since 1997. We handle residential, commercial, recreational land and farmland.
Our current web site design is outdated and needs a more modern look. We are open to all design ideas but would want them to reflect our small town rural tradition and heritage.
The functionality and features of the site will remain the same. Your design will have to accommodate the existing features on the site. I have a programmer who will take the design you provide and retrofit the existing site functionality with it.
The deliverable will be a .psd file that can be converted to html for a site template. (We will do the conversion.)
The existing site is at:
http://www.tomwendellhomesales.example/home.asp
Please take time to visit the site and note the current functionality the site has: property search, real estate news feed, mortgage rate feed, listings, navigation bar will need to handle existing links and expand to handle other future page links. The template provided will need to accommodate these features.
The current page logo can be used in the design or we are open to a redesign of that as well if needed to go with the design better.
Updates
Project Deadline Extended
Reason: Haven't had anything satisfactory yet.
Target Market(s)
Middle income households and farmers looking for the services of a real estate agent or auctioneer.
Industry/Entity Type
Real Estate
Look and feel

```html
<!DOCTYPE html>
<html lang="en">
<head>
<meta charset="utf-8">
<title>Wendell Home Sales and Land Company</title>
<link href="https://fonts.googleapis.com/css2?family=PT+Sans:wght@400;700&family=Arimo:wght@400;700&display=swap" rel="stylesheet">
<style>
:root{
  --lime:#b4dc26;
  --lime-dark:#7ab80a;
  --nav:#2a140c;
  --rust:#97461c;
  --cocoa:#45281c;
  --footer:#250f06;
  --orange:#e8682a;
  --white:#ffffff;
  --row-light:#f1d7ce;
  --row-dark:#dba99a;
  --link-blue:#2f64d6;
  --ribbon:#2a5fa8;
  --red:#d9321a;
}
*{margin:0;padding:0;box-sizing:border-box}
html,body{width:1116px;height:1200px;overflow:hidden}
body{position:relative;background:var(--lime);font-family:"PT Sans",sans-serif;color:var(--white)}
.abs{position:absolute}

.brand{left:30px;top:40px;display:flex;align-items:center;gap:10px}
.brand-mark{width:26px;height:26px;background:var(--white)}
.brand-name{font-family:"PT Sans",sans-serif;font-weight:400;font-size:38px;color:var(--white);letter-spacing:1px}

.contact{left:828px;top:58px;font-weight:700;font-size:17px;line-height:19px}
.contact-icons{left:950px;top:62px;display:flex;gap:18px}

.main-nav{left:13px;top:153px;width:1090px;height:39px;background:var(--nav);display:flex;list-style:none}
.main-nav li{font-weight:700;font-size:13px;line-height:39px;padding:0 19px 0 32px;border-right:1px solid #3f2418}
.main-nav li:first-child{padding-left:32px}
.main-nav li:last-child{border-right:none}

.skyline{left:0;top:192px;width:1116px;height:364px;background:linear-gradient(180deg,var(--lime) 0%,#9ccc18 45%,var(--lime-dark) 100%)}
.welcome-banner{right:46px;top:458px;font-weight:700;font-size:21px}

.feature-band{left:0;top:556px;width:1116px;height:114px;background:var(--rust);border-top:6px solid var(--white);border-bottom:4px solid var(--white)}
.feature{top:516px;width:200px;text-align:center}
.feature-icon{width:92px;height:92px;margin:0 auto;border-radius:50%;background:var(--nav);border:5px solid var(--white);display:flex;align-items:center;justify-content:center}
.feature-label{margin-top:20px;font-weight:700;font-size:13px}

.content{left:0;top:674px;width:1116px;height:362px;background:var(--cocoa)}
.intro{left:46px;top:708px;width:545px}
.intro h1{font-size:21px;font-weight:700;color:var(--orange);margin-bottom:10px}
.intro p{font-family:"Arimo",sans-serif;font-size:11.4px;line-height:19.6px;text-align:justify;margin-bottom:19.6px}

.featured{left:644px;top:715px;width:416px;height:280px;background:var(--white)}
.featured-title{left:88px;top:21px;font-family:"Arimo",sans-serif;font-weight:700;font-size:19px;color:var(--red)}
.featured-house{left:335px;top:8px;width:48px;height:44px;background:#8a4a3a}
.ribbon{left:-14px;top:-8px}
.listings{left:14px;top:55px;width:378px;list-style:none}
.listings li{height:33px;line-height:33px;padding-left:18px;font-family:"Arimo",sans-serif;font-size:11.6px;color:#3a2a25;background:var(--row-light);margin-bottom:0}
.listings li:nth-child(even){background:var(--row-dark)}
.scrollbar{left:398px;top:55px;width:16px;height:218px;background:#eef2fa;border:1px solid #b9c6de}
.scroll-thumb{left:1px;top:17px;width:12px;height:62px;background:#c9d8f4;border:1px solid #8ea6d6;border-radius:2px}
.updates{left:150px;top:243px;width:230px;text-align:center;font-family:"Arimo",sans-serif;font-weight:700;font-size:13px;line-height:15px;color:var(--link-blue)}

.mailing{left:0;top:1036px;width:1116px;height:76px;background:var(--lime)}
.mailing-label{left:49px;top:1063px;font-family:"Arimo",sans-serif;font-size:17.5px;color:#111}
.mailing-input{left:408px;top:1055px;width:424px;height:38px;background:var(--white);border:none}
.mailing-submit{left:832px;top:1052px;width:44px;height:44px;border-radius:5px;background:#1fa6dc;display:flex;align-items:center;justify-content:center}
.social{left:881px;top:1055px;display:flex;gap:3px}
.social span{width:31px;height:38px;background:#efe6cf;border:1px solid #d7c9a8}

.footer{left:0;top:1112px;width:1116px;height:88px;background:var(--footer)}
</style>
</head>
<body>
  <div class="abs brand"><span class="brand-mark"></span><span class="brand-name">WENDELL</span></div>

  <div class="abs contact">Phone<br>(555) 014-2290</div>
  <div class="abs contact-icons">
    <svg width="38" height="28" viewBox="0 0 38 28"><ellipse cx="19" cy="12" rx="18" ry="11" fill="#fff"/><path d="M10 20 L7 28 L17 22Z" fill="#fff"/></svg>
    <svg width="38" height="24" viewBox="0 0 38 24"><rect x="1" y="1" width="36" height="22" fill="#fff"/><path d="M1 1 L19 14 L37 1" fill="none" stroke="#b4dc26" stroke-width="2"/></svg>
  </div>

  <ul class="abs main-nav">
    <li>HOME</li><li>ABOUT US</li><li>OPEN HOUSE</li><li>TESTIMONIALS</li><li>CALCULATORS</li><li>LINKS</li><li>CONTACT US</li>
  </ul>

  <div class="abs skyline" role="img" aria-label="Green city skyline silhouette"></div>
  <div class="abs welcome-banner">Welcome to Wendell Home Sales and Land Company's web site.</div>

  <div class="abs feature-band"></div>
  <div class="abs feature" style="left:72px">
    <div class="feature-icon"><svg width="48" height="44" viewBox="0 0 48 44"><path d="M24 3 L45 21 H39 V41 H9 V21 H3Z" fill="none" stroke="#fff" stroke-width="3"/><rect x="14" y="25" width="8" height="8" fill="#fff"/><rect x="27" y="25" width="8" height="16" fill="#fff"/></svg></div>
    <div class="feature-label">OPEN HOUSE LISTINGS</div>
  </div>
  <div class="abs feature" style="left:323px">
    <div class="feature-icon"><svg width="30" height="40" viewBox="0 0 30 40"><rect x="1" y="1" width="28" height="38" rx="3" fill="#fff"/><rect x="5" y="5" width="20" height="8" fill="#2a140c"/><g fill="#2a140c"><rect x="5" y="17" width="5" height="4"/><rect x="12.5" y="17" width="5" height="4"/><rect x="20" y="17" width="5" height="4"/><rect x="5" y="24" width="5" height="4"/><rect x="12.5" y="24" width="5" height="4"/><rect x="20" y="24" width="5" height="4"/><rect x="5" y="31" width="5" height="4"/><rect x="12.5" y="31" width="5" height="4"/><rect x="20" y="31" width="5" height="4"/></g></svg></div>
    <div class="feature-label">CALCULATORS</div>
  </div>
  <div class="abs feature" style="left:552px">
    <div class="feature-icon"><svg width="46" height="34" viewBox="0 0 46 34"><circle cx="10" cy="10" r="8" fill="#fff"/><path d="M15 14 L42 28 L40 32 L36 30 L34 33 L31 28 L13 18Z" fill="#fff"/></svg></div>
    <div class="feature-label">FIRST TIME BUYERS</div>
  </div>
  <div class="abs feature" style="left:802px">
    <div class="feature-icon"><svg width="50" height="36" viewBox="0 0 50 36"><g fill="#fff"><circle cx="16" cy="14" r="10"/><circle cx="30" cy="12" r="11"/><circle cx="40" cy="19" r="8"/><circle cx="10" cy="21" r="8"/><rect x="10" y="16" width="30" height="13"/><path d="M14 27 L10 35 L22 28Z"/></g></svg></div>
    <div class="feature-label">TESTIMONIALS</div>
  </div>

  <div class="abs content"></div>
  <section class="abs intro">
    <h1>WELCOME HOME</h1>
    <p>Welcome to Wendell Home Sales and Land Company's web site. Your visit here will make it easy for you to find the real estate you are seeking by using our simple search menu. Not only will you find area real estate listings, but also other items such as the latest mortgage rates and real estate news, and businesses that are associated with buying and selling homes and farmland. I will be servicing the needs of the people in the Alder Creek, Millbrook, Harlow, Ridgefield, Oakmont and all area communities.</p>
    <p>I have been in the real estate business since 1997 and have been a broker since 1999. I'm looking forward to marketing your property for "top dollar" or finding that "perfect" piece of property you desire whether it be residential, commercial, recreational, farmland (statewide), country property, or 1031 exchange. I am also a member of the Prairie Valley Multiple Listing Service.</p>
  </section>

  <section class="abs featured">
    <div class="abs featured-title">HOUSE NOW FEATURED</div>
    <div class="abs featured-house" role="img" aria-label="Small house illustration"></div>
    <ul class="abs listings">
      <li>1153 Maple Ridge Dr. Elmford, 60000 3/2/2 1410 sqft. $1295.00***</li>
      <li>1153 Maple Ridge Dr. Elmford, 60000 3/2/2 1410 sqft. $1295.00***</li>
      <li>1153 Maple Ridge Dr. Elmford, 60000 3/2/2 1410 sqft. $1295.00***</li>
      <li>1153 Maple Ridge Dr. Elmford, 60000 3/2/2 1410 sqft. $1295.00***</li>
      <li>1153 Maple Ridge Dr. Elmford, 60000 3/2/2 1410 sqft. $1295.00***</li>
    </ul>
    <div class="abs scrollbar"><div class="abs scroll-thumb"></div></div>
    <div class="abs updates">CHECK BACK FOR OUR WEEKLY UPDATES AND NEW LISTINGS!!</div>
    <svg class="abs ribbon" width="140" height="110" viewBox="0 0 140 110"><path d="M0 70 L78 0 L136 0 L6 104Z" fill="var(--ribbon)"/><text x="0" y="0" transform="translate(32 78) rotate(-40)" fill="#fff" font-family="Arimo, sans-serif" font-weight="700" font-size="16">VIEW NOW</text></svg>
  </section>

  <div class="abs mailing"></div>
  <div class="abs mailing-label">join our mailing list and receive the best deals!</div>
  <input class="abs mailing-input" type="text" aria-label="Email address">
  <div class="abs mailing-submit"><svg width="30" height="26" viewBox="0 0 30 26"><path d="M2 9 H16 V2 L28 13 L16 24 V17 H2Z" fill="#d7f02a"/></svg></div>
  <div class="abs social"><span></span><span></span><span></span></div>

  <div class="abs footer"></div>
</body>
</html>
```